6 Sizes Set - Static Banners

We have an html template for our newsletter which include graphic elements and we need images to populate these fixed Grey spaces.

Attachment 1: PLEASE READ FULL Graphic Brief is the complete brief describing all fine details.

Attachment 2: layout, shows the example of template

Attachment 3: We need the 6 image sizes (i.e. different fonts, backgrounds, colors, casino icons) – attached Styles Folder for an idea of the variety. These are just a few examples.

Target Market(s)

global

Industry/Entity Type

Casino

Requirements
Must have
• Refer to attach Full brief, for complete explanation
Nice to have
• Second Place: refer to Screenshot
Perfect example of what to submit

```html
<!DOCTYPE html>
<html lang="en">
<head>
<meta charset="utf-8">
<title>Newsletter – Casino</title>
<link rel="stylesheet" href="https://fonts.googleapis.com/css2?family=Ubuntu:ital,wght@0,400;0,500;0,700;1,400&family=Cinzel:wght@400;500&family=Open+Sans:ital,wght@0,400;0,700;1,400&display=swap">
<style>
  :root{
    --page:#ededed;
    --white:#ffffff;
    --blue:#4aa0e8;
    --blue-dark:#2f86d6;
    --blue-light:#7cc0f4;
    --text:#222222;
    --grey:#8d8d8d;
    --grey-light:#a5a5a5;
    --nav-bar:#d4d4d4;
    --gold:#e3bd62;
    --icon:#3c3c3c;
  }
  *{box-sizing:border-box;margin:0;padding:0}
  html,body{width:1200px;height:1042px;overflow:hidden}
  body{background:var(--page);font-family:"Open Sans",Arial,sans-serif;color:var(--text);position:relative}

  .preheader{position:absolute;top:8px;left:0;width:1216px;text-align:center;font-size:15px;color:var(--grey)}
  .preheader b{color:var(--text);font-weight:700}
  .social{position:absolute;top:8px;left:966px;display:flex;gap:12px}
  .social span{width:22px;height:22px;border-radius:50%;background:var(--icon);display:block}

  .logo-box{position:absolute;left:80px;top:53px;width:408px;height:62px;background:var(--white);border-radius:8px;box-shadow:0 10px 10px -6px rgba(0,0,0,.25);display:flex;align-items:center;padding-left:28px}
  .logo{font-family:"Ubuntu",sans-serif;font-size:44px;font-weight:500;color:var(--blue)}

  .nav{position:absolute;top:74px;right:80px;display:flex;gap:28px}
  .nav a{font-family:"Ubuntu",sans-serif;font-size:15px;color:var(--grey);text-decoration:none;padding-bottom:6px;border-bottom:5px solid var(--nav-bar)}

  .hero{position:absolute;left:80px;top:141px;width:1040px;height:352px;background:var(--white)}
  .hero-shadow{position:absolute;left:140px;top:488px;width:920px;height:20px;border-radius:50%;background:radial-gradient(ellipse at center,rgba(0,0,0,.35),rgba(0,0,0,0) 70%)}
  .hero-title{position:absolute;left:32px;top:32px;width:344px;height:48px;background:var(--blue);color:var(--white);font-family:"Ubuntu",sans-serif;font-weight:400;font-size:32px;line-height:48px;padding-left:10px;box-shadow:0 4px 4px -2px rgba(0,0,0,.2)}
  .hero-copy{position:absolute;left:32px;top:116px;width:316px;font-size:18px;line-height:26px}
  .btn{position:absolute;left:32px;top:259px;width:328px;height:59px;background:linear-gradient(var(--blue-light),var(--blue-dark));color:var(--white);font-family:"Ubuntu",sans-serif;font-weight:500;font-size:26px;line-height:59px;padding-left:28px;text-decoration:none}
  .btn svg{position:absolute;right:10px;top:7px}
  .hero-photo{position:absolute;left:386px;top:6px;width:626px;height:336px;background:
      radial-gradient(ellipse 38% 55% at 62% 60%,rgba(235,230,225,.55),rgba(235,230,225,0) 70%),
      linear-gradient(180deg,rgba(0,0,0,0) 82%,#1f6a2e 90%,#174f22 100%),
      linear-gradient(90deg,#2a0e0d 0%,#4a1c1a 35%,#3a1513 65%,#24100f 100%)}
  .hero-photo span{position:absolute;left:38px;top:84px;font-family:"Cinzel",serif;font-size:36px;color:var(--white);letter-spacing:1px}

  .salutation{position:absolute;top:527px;width:1200px;text-align:center;font-family:"Ubuntu",sans-serif;font-weight:500;font-size:32px;color:var(--grey-light)}
  .lead{position:absolute;top:566px;width:1200px;text-align:center;font-style:italic;font-size:25px;color:var(--grey-light)}

  .card{position:absolute;top:632px;width:336px;height:320px;background:var(--white);box-shadow:0 0 3px rgba(0,0,0,.08)}
  .card-art{position:absolute;left:8px;top:8px;width:320px;height:200px}
  .card-art .pointer{position:absolute;left:0;top:92px;width:0;height:0;border-top:10px solid transparent;border-bottom:10px solid transparent;border-left:10px solid var(--white)}
  .card-art .band{position:absolute;left:0;bottom:0;width:100%;height:64px;background:linear-gradient(#2a2a2a,#0c0c0c);color:var(--gold);font-family:"Cinzel",serif;font-weight:500;font-size:24px;text-align:center;line-height:64px;white-space:nowrap}
  .art-spins{background:radial-gradient(ellipse 50% 55% at 50% 40%,#b8862c,#6a4a1a 55%,#1c1c1c 100%)}
  .art-cash{background:radial-gradient(circle at 70% 20%,#ffe066,#f5a623 40%,#c0392b 75%,#1a1a1a 100%)}
  .art-jackpot{background:linear-gradient(135deg,#2a1a0c,#c9862a 45%,#9a2a18 70%,#3a1a10)}
  .card-info{position:absolute;left:8px;top:218px;width:320px;height:94px;background:var(--blue);color:var(--white);padding:0 10px}
  .card-info h3{font-family:"Ubuntu",sans-serif;font-weight:400;font-size:26px;line-height:38px;border-bottom:2px solid rgba(255,255,255,.45)}
  .card-info p{font-size:16px;line-height:22px;margin-top:6px;width:240px}
  .card-info svg{position:absolute;right:10px;top:40px}
</style>
</head>
<body>
  <p class="preheader">If you can not view this email, <b>click here.</b></p>
  <div class="social" aria-label="Social links"><span></span><span></span><span></span><span></span><span></span></div>

  <div class="logo-box"><span class="logo">YOURCOMPANY</span></div>

  <nav class="nav">
    <a href="#">VIEW SITE</a>
    <a href="#">ABOUT US</a>
    <a href="#">TEAM WORK</a>
    <a href="#">CONTACT</a>
  </nav>

  <div class="hero-shadow"></div>
  <section class="hero">
    <h1 class="hero-title">Title Here</h1>
    <p class="hero-copy">Lorem ipsum dolor sit amet, consectetur adipiscing elit. Cras fringilla ligula sit amet dui tempor hendrerit.</p>
    <a class="btn" href="#">Register for FREE
      <svg width="44" height="44" viewBox="0 0 44 44"><circle cx="22" cy="22" r="20" fill="#e8f4fd" stroke="#ffffff" stroke-width="2"/><circle cx="22" cy="22" r="15" fill="#3b9be6"/><path d="M18 14 L30 22 L18 30 Z" fill="#ffffff"/></svg>
    </a>
    <div class="hero-photo" role="img" aria-label="Photo of a high roller at a casino table throwing poker chips in the air"><span>HIGH ROLLERS</span></div>
  </section>

  <h2 class="salutation">Saudation</h2>
  <p class="lead">Lorem ipsum dolor sit amet, consectetur adipiscing elit. Donec id.</p>

  <article class="card" style="left:85px">
    <div class="card-art art-spins" role="img" aria-label="Slot machine reels showing three sevens"><i class="pointer"></i><div class="band">FREE SPINS GIVEAWAY</div></div>
    <div class="card-info"><h3>Featured #1</h3><p>Vestibulum posuere velit non turpis iaculis eget pharetra.</p>
      <svg width="44" height="44" viewBox="0 0 44 44"><circle cx="22" cy="22" r="20" fill="#e8f4fd" stroke="#ffffff" stroke-width="2"/><circle cx="22" cy="22" r="15" fill="#3b9be6"/><path d="M18 14 L30 22 L18 30 Z" fill="#ffffff"/></svg></div>
  </article>

  <article class="card" style="left:432px">
    <div class="card-art art-cash" role="img" aria-label="Stacks of casino chips with playing cards on a golden burst"><i class="pointer"></i><div class="band">BEST CASHBACKS</div></div>
    <div class="card-info"><h3>Featured #1</h3><p>Vestibulum posuere velit non turpis iaculis eget pharetra.</p>
      <svg width="44" height="44" viewBox="0 0 44 44"><circle cx="22" cy="22" r="20" fill="#e8f4fd" stroke="#ffffff" stroke-width="2"/><circle cx="22" cy="22" r="15" fill="#3b9be6"/><path d="M18 14 L30 22 L18 30 Z" fill="#ffffff"/></svg></div>
  </article>

  <article class="card" style="left:779px">
    <div class="card-art art-jackpot" role="img" aria-label="Jackpot sign on a slot machine"><i class="pointer"></i><div class="band">FREE CASH GIVEAWAY</div></div>
    <div class="card-info"><h3>Featured #1</h3><p>Vestibulum posuere velit non turpis iaculis eget pharetra.</p>
      <svg width="44" height="44" viewBox="0 0 44 44"><circle cx="22" cy="22" r="20" fill="#e8f4fd" stroke="#ffffff" stroke-width="2"/><circle cx="22" cy="22" r="15" fill="#3b9be6"/><path d="M18 14 L30 22 L18 30 Z" fill="#ffffff"/></svg></div>
  </article>
</body>
</html>
```